Ledgerwise Reach - B2B Demand Generation Website Project

We need a fully functional website for www.ledgerwisereach.example. We are a B2B Demand Generation company, based in London, working with companies such as QRT, VKD, Norvex, Brindlow, Tarvo generating them sales leads for their sales teams. We run this through digital marketing newsletter promotions and have a network of websites. Content syndication, data, demand generation, online marketing. Our logo has just been redone (attached) and we have a holding page already which i would like to use the style / colours. Our logo is bright and vibrant but i dont want the site to be a rainbow. We are expensive, classy, professorial, B2B, intelligent.

Home
About Us
Our Services
Prospora & QA Technology
Intent Data
Testimonials
Contact Us
Updates

Target Market(s)

B2B Marketers (QRT, Velquarion, Tarvo, VKD, Opal Reach, Driftmoor, Harlow Quantis, Technology Companies, Data Companies, Marketing Teams, Tumbleden.

Industry/Entity Type

Marketing

Coding

Coded - Design and coding required

Number of Pages Required

5+ page

Font styles to use
Sans Serif

Requirements
Must have
• Home
About Us
Our Services
Prospora & QA Technology
Intent Data
Testimonials
Contact Us

Simple Pages.

Look classy, intelligent, data experts. I like the video homepages were the image moves at the top. Very soft animation.
Nice to have
• Websites i like:

https://www.vkd.example/
https://www.brevantor.example/
https://www.plumfieldsites.example.co.uk/

Ledgerwise Reach - The Demand Generation Company
Should not have
• Glimpsevault crap images

```html
<!DOCTYPE html>
<html lang="en">
<head>
<meta charset="utf-8">
<title>Ledgerwise Reach - The Demand Generation Company</title>
<link href="https://fonts.googleapis.com/css2?family=Poppins:wght@400;500;600;700&display=swap" rel="stylesheet">
<style>
:root{
  --navy:#0b2545;
  --navy-deep:#0a1838;
  --blue:#124a8a;
  --sky:#1e7fd6;
  --text:#1d2433;
  --muted:#6b7383;
  --line:#e6e9f0;
  --wash:#f5f6fa;
  --accent:#e23b3b;
  --violet:#6a4cf0;
  --white:#ffffff;
}
*{box-sizing:border-box;margin:0;padding:0}
html,body{width:1200px;height:4556px;overflow:hidden}
body{position:relative;font-family:"Poppins",sans-serif;color:var(--text);background:var(--white)}
.abs{position:absolute}
a{color:inherit;text-decoration:none}

/* header */
.logo{left:235px;top:16px;display:flex;flex-direction:column;align-items:center;width:160px}
.logo-mark{width:24px;height:24px;border-radius:50%;border:3px solid var(--accent)}
.logo-name{font-size:18px;font-weight:500;color:var(--accent);line-height:1.2;margin-top:3px;white-space:nowrap}
.logo-tag{font-size:7px;color:var(--violet);white-space:nowrap}
.phone{left:760px;top:18px;font-size:13px;color:var(--navy);font-weight:500;display:flex;align-items:center;gap:6px}
.social-top{left:893px;top:16px;display:flex;gap:6px}
.social-top span{width:20px;height:20px;border-radius:50%;border:1px solid #8fa2c4}
.nav{left:484px;top:56px;display:flex;align-items:center;font-size:11px;color:var(--text)}
.nav a{padding:0 12px}
.nav .active{background:var(--blue);color:var(--white);border-radius:14px;padding:6px 20px;margin-right:6px}

/* hero */
.hero-art{left:0;top:97px;width:1200px;height:640px}
.hero-title{left:535px;top:228px;font-size:44px;font-weight:700;color:var(--white);line-height:1.15}
.btn-light{left:535px;top:362px;width:100px;height:28px;border-radius:14px;background:var(--white);color:var(--blue);font-size:11px;font-weight:600;display:flex;align-items:center;justify-content:center}

/* buttons */
.btn{height:32px;padding:0 18px;display:inline-flex;align-items:center;gap:8px;font-size:11px;font-weight:500;border-radius:2px}
.btn-solid{background:var(--blue);color:var(--white)}
.btn-ghost{border:1px solid #c8cfdb;color:var(--blue);background:var(--white)}
.dot{width:10px;height:10px;border-radius:50%;display:inline-block}
.btn-solid .dot{background:var(--white)}
.btn-ghost .dot{background:var(--blue)}

/* intro */
.intro{left:235px;top:820px;width:320px}
.intro .lead{font-size:13.5px;line-height:20px;color:var(--text)}
.intro .small{font-size:10.5px;line-height:17.5px;color:var(--muted);margin-top:22px}
.intro .btn{margin-top:20px}
.tile{width:124px;height:114px;border-radius:4px;color:var(--white);font-size:9.5px;text-align:center;display:flex;flex-direction:column;align-items:center;justify-content:flex-end;padding-bottom:16px;line-height:1.4;box-shadow:0 14px 26px rgba(20,30,80,.22)}
.tile svg{margin-bottom:10px}
.t-orange{left:839px;top:799px;background:linear-gradient(135deg,#f9c623,#f39a12)}
.t-violet{left:740px;top:850px;background:linear-gradient(135deg,#7a45f2,#5a37d8)}
.t-red{left:654px;top:924px;background:linear-gradient(135deg,#ef4a3f,#d8262b)}
.t-blue{left:822px;top:968px;background:linear-gradient(135deg,#2ca3f0,#1a6fd8)}

/* services */
.wash{left:0;top:1255px;width:1200px;height:520px}
.sec-title{width:1200px;left:0;text-align:center;font-size:19px;font-weight:600;color:var(--navy)}
.sec-sub{width:1200px;left:0;text-align:center;font-size:10px;line-height:17px;color:var(--muted)}
.steps{left:340px;top:1282px;width:520px;height:22px}
.step{position:absolute;top:0;width:20px;height:20px;border-radius:50%;border:1px solid var(--violet);font-size:9px;display:flex;align-items:center;justify-content:center;color:var(--violet);background:var(--white)}
.step.on{background:var(--blue);border-color:var(--blue);color:var(--white)}
.card{width:250px;text-align:center}
.card.raised{background:var(--white);box-shadow:0 14px 40px rgba(30,40,80,.10);height:282px}
.card .icon{width:46px;height:50px;margin:0 auto;border-radius:6px;background:linear-gradient(135deg,#7e6cf5,#3aa0f2)}
.card h3{font-size:12px;font-weight:500;color:var(--navy);margin-top:34px}
.card p{font-size:9.5px;line-height:17.5px;color:var(--muted);margin:12px auto 0;width:200px}
.card .btn{margin-top:26px}

/* who we work with */
.who{left:235px;top:1890px;width:290px}
.who-mark{width:46px;height:46px;border-radius:50%;background:var(--white);box-shadow:0 6px 18px rgba(30,40,80,.12);display:flex;align-items:center;justify-content:center}
.who-mark span{width:20px;height:20px;border-radius:50%;border:3px solid var(--accent)}
.who h2{font-size:16px;font-weight:500;color:var(--navy);margin-top:26px}
.who p{font-size:10.5px;line-height:18.5px;color:var(--muted);margin-top:20px}
.btn-row{display:flex;gap:12px;margin-top:22px}
.brand{background:var(--white);box-shadow:0 8px 26px rgba(30,40,80,.10);display:flex;align-items:center;justify-content:center;font-size:14px;font-weight:600;color:var(--navy)}

/* split rows */
.split-wash{left:0;top:2442px;width:600px;height:405px;background:var(--wash)}
.photo{background:linear-gradient(135deg,#8a8f99,#c9c3ba 45%,#5d6472)}
.split h2{font-size:16.5px;font-weight:500;line-height:24px;color:var(--navy)}
.split ul{list-style:none;margin-top:28px}
.split li{font-size:10.5px;line-height:21px;color:var(--muted);padding-left:22px;position:relative}
.split li::before{content:"";position:absolute;left:2px;top:9px;width:3px;height:3px;border-radius:50%;background:var(--muted)}
.qa h2{font-size:26px;font-weight:500;color:var(--navy)}
.qa p{font-size:10.5px;line-height:18.8px;color:var(--muted);margin-top:20px}

/* stats */
.stats{left:0;top:3354px;width:1200px;height:419px;background:var(--navy)}
.stats-art{left:380px;top:0;width:820px;height:419px;background:linear-gradient(160deg,rgba(11,37,69,0) 20%,rgba(120,70,60,.35) 65%,rgba(11,37,69,0) 95%)}
.stat{color:var(--white)}
.stat h3{font-size:31px;font-weight:400;line-height:37px}
.stat p{font-size:12px;margin-top:6px}

/* testimonials */
.quote-card{left:359px;top:3919px;width:480px;height:278px;background:var(--white);box-shadow:0 12px 40px rgba(30,40,80,.08);text-align:center}
.avatar{width:40px;height:40px;border-radius:50%;background:linear-gradient(135deg,#bfc4cc,#6f7682);margin:42px auto 0}
.quote-card h4{font-size:11px;font-weight:500;margin-top:8px;color:var(--navy)}
.quote-card .role{font-size:8.5px;color:var(--muted);margin-top:2px}
.quote-card p{font-size:9.8px;line-height:17.5px;color:var(--muted);width:410px;margin:22px auto 0}
.dots{display:flex;gap:6px;justify-content:center;margin-top:20px;align-items:center}
.dots span{width:4px;height:4px;border-radius:50%;background:#c6ccd8}
.dots .on{width:9px;height:9px;background:none;border:1px solid var(--sky)}
.arrow{width:30px;height:30px;border-radius:50%;display:flex;align-items:center;justify-content:center}

/* footer */
.footer{left:0;top:4289px;width:1200px;height:267px;background:var(--navy-deep)}
.f-logo{left:235px;top:4354px;width:166px;height:74px;background:var(--white);border-radius:3px;display:flex;flex-direction:column;align-items:center;justify-content:center}
.f-logo .logo-name{font-size:15px}
.f-col h5{font-size:10.5px;font-weight:600;color:var(--white)}
.f-col a{display:block;font-size:9.5px;color:#a9b3c9;margin-top:10px}
.copy{left:240px;top:4452px;font-size:8.5px;color:#a9b3c9}
.f-social{left:859px;top:4405px;display:flex;gap:8px}
.f-social span{width:20px;height:20px;border-radius:50%;background:#2a3a64}
.f-social .on{background:var(--sky)}
</style>
</head>
<body>

<!-- header -->
<a class="abs logo" href="#">
  <span class="logo-mark"></span>
  <span class="logo-name">Ledgerwise Reach</span>
  <span class="logo-tag">The Demand Generation Company</span>
</a>
<div class="abs phone">
  <svg width="16" height="14" viewBox="0 0 16 14"><path d="M3 1c1 0 2 2 2 3s-1 1-1 2 2 3 3 3 1-1 2-1 3 1 3 2-1 3-3 3C6 13 1 8 1 4 1 2 2 1 3 1z" fill="none" stroke="#124a8a" stroke-width="1.3"/></svg>
  020 7946 0183
</div>
<div class="abs social-top"><span></span><span></span><span></span></div>
<nav class="abs nav">
  <a class="active" href="#">Home</a><a href="#">About</a><a href="#">Services</a><a href="#">Technology</a><a href="#">Intent Data</a><a href="#">Testimonials</a><a href="#">Contact</a>
</nav>

<!-- hero -->
<svg class="abs hero-art" viewBox="0 0 1200 640" role="img" aria-label="Hero visual: glowing blue abstract tunnel with brand emblem">
  <defs>
    <linearGradient id="heroBlue" x1="0" y1="0" x2="1" y2="1">
      <stop offset="0" stop-color="#0a5fb0"/><stop offset=".55" stop-color="#1a86d6"/><stop offset="1" stop-color="#0b2f6b"/>
    </linearGradient>
  </defs>
  <path d="M40 0H1200V110L360 630Q300 660 250 620L0 360V0Z" fill="#ece8fb"/>
  <path d="M0 0H1200V40L330 600Q285 628 250 590L0 320Z" fill="url(#heroBlue)"/>
</svg>
<h1 class="abs hero-title">B2B Demand<br>Generation</h1>
<a class="abs btn-light" href="#">Get Started</a>

<!-- intro -->
<section class="abs intro">
  <p class="lead">Ledgerwise Reach offers multi-channel demand generation services to publishers and technology vendors through our network of lead generation websites and native speaking telemarketing agents.</p>
  <p class="small">Whether looking for MQL, ABM or BANT campaigns, Ledgerwise Reach can assist you in delivering your demand generation strategy and generate pipeline for your sales teams and/or channel partners.</p>
  <a class="btn btn-solid" href="#">Learn More <span class="dot"></span></a>
</section>
<div class="abs tile t-violet"><svg width="24" height="22" viewBox="0 0 24 22" fill="none" stroke="#fff" stroke-width="1.4"><rect x="2" y="2" width="20" height="16"/><path d="M2 7h20M6 11h8M6 14h5"/></svg>Account Based<br>Marketing Leads</div>
<div class="abs tile t-orange"><svg width="24" height="24" viewBox="0 0 24 24" fill="none" stroke="#fff" stroke-width="1.4"><circle cx="12" cy="12" r="9"/><path d="M3 12h18M12 3c3 3 3 15 0 18M12 3c-3 3-3 15 0 18"/></svg>QA<br>Technology</div>
<div class="abs tile t-red"><svg width="20" height="24" viewBox="0 0 20 24" fill="none" stroke="#fff" stroke-width="1.4"><rect x="2" y="2" width="16" height="20"/><path d="M6 8h8M6 12h8M6 16h5"/></svg>Marketing<br>Qualified Leads</div>
<div class="abs tile t-blue"><svg width="26" height="24" viewBox="0 0 26 24" fill="none" stroke="#fff" stroke-width="1.4"><circle cx="8" cy="7" r="3"/><path d="M3 20c0-5 10-5 10 0M16 14l8-8M19 6h5v5"/></svg>Sales Qualified<br>Lead / BANT</div>

<!-- services -->
<svg class="abs wash" viewBox="0 0 1200 520" aria-hidden="true">
  <path d="M0 40Q300 0 600 30T1200 0V300Q900 520 500 470T0 520Z" fill="#f5f6fa"/>
  <path d="M1200 60L820 520" stroke="#eef0f6" stroke-width="2" fill="none"/>
</svg>
<h2 class="abs sec-title" style="top:1182px">Our Services</h2>
<p class="abs sec-sub" style="top:1214px">Ledgerwise Reach can deliver high quality sales leads from any<br>country in the world.</p>
<div class="abs steps">
  <svg class="abs" style="left:0;top:10px" width="520" height="2"><line x1="20" y1="1" x2="500" y2="1" stroke="#dfe3ec"/></svg>
  <span class="step" style="left:0">1</span>
  <span class="step on" style="left:250px">2</span>
  <span class="step" style="left:500px">3</span>
</div>
<article class="abs card" style="left:212px;top:1362px">
  <div class="icon" role="img" aria-label="Illustration for marketing qualified leads"></div>
  <h3>Marketing Qualified Leads</h3>
  <p>A Marketing Qualified Lead (MQL) is a prospect that has expressed an interest in what your brand has to offer.</p>
</article>
<article class="abs card raised" style="left:475px;top:1287px;padding-top:75px">
  <div class="icon" role="img" aria-label="Illustration for account based marketing leads"></div>
  <h3>Account Based Marketing Leads</h3>
  <p>ABM is a strategy that directs marketing resources to engaging a specific set of target accounts.</p>
  <a class="btn btn-solid" href="#">Learn More <span class="dot"></span></a>
</article>
<article class="abs card" style="left:737px;top:1362px">
  <div class="icon" role="img" aria-label="Illustration for QA technology"></div>
  <h3>QA Technology</h3>
  <p>Prospora is a proprietary lead verification platform from Ledgerwise Reach that aims to sift out invalid leads</p>
</article>

<!-- who we work with -->
<svg class="abs" style="left:700px;top:2050px" width="500" height="400" aria-hidden="true"><path d="M0 60Q300 200 500 400" stroke="#eef0f6" stroke-width="2" fill="none"/></svg>
<section class="abs who">
  <div class="who-mark"><span></span></div>
  <h2>Who we work with</h2>
  <p>Ledgerwise Reach offer expert demand generation support, from providing detailed leads of qualified decision-makers, to a comprehensive lead generation and SQL service.</p>
  <div class="btn-row">
    <a class="btn btn-solid" href="#">Learn More <span class="dot"></span></a>
    <a class="btn btn-ghost" href="#">Support <span class="dot"></span></a>
  </div>
</section>
<div class="abs brand" style="left:571px;top:1967px;width:138px;height:74px">VKD</div>
<div class="abs brand" style="left:739px;top:1908px;width:118px;height:85px">Tarvo</div>
<div class="abs brand" style="left:922px;top:1866px;width:106px;height:78px">Workvane</div>
<div class="abs brand" style="left:1046px;top:1929px;width:92px;height:71px">Calderix</div>
<div class="abs brand" style="left:850px;top:2007px;width:115px;height:87px">Cloudhelm</div>
<div class="abs brand" style="left:986px;top:2050px;width:140px;height:70px">Orlinde</div>
<div class="abs brand" style="left:694px;top:2062px;width:131px;height:120px">QRT</div>
<div class="abs brand" style="left:894px;top:2133px;width:106px;height:90px">Penwick</div>
<div class="abs brand" style="left:797px;top:2244px;width:136px;height:69px">Tidebrook</div>

<!-- split: leads -->
<div class="abs split-wash"></div>
<section class="abs split" style="left:171px;top:2516px;width:400px">
  <h2>Ledgerwise Reach can deliver high quality<br>sales leads from any country in the world</h2>
  <ul>
    <li>Breakdown by geography, job title, role and responsibility</li>
    <li>Targeting through previous research and buying intention</li>
    <li>Email dispatch to selected individuals</li>
    <li>Extensive telemarketing options</li>
  </ul>
  <div class="btn-row">
    <a class="btn btn-solid" href="#">Learn More <span class="dot"></span></a>
    <a class="btn btn-ghost" href="#">Support <span class="dot"></span></a>
  </div>
</section>
<div class="abs photo" style="left:600px;top:2442px;width:600px;height:405px" role="img" aria-label="Photo: colleagues talking together in a bright office"></div>

<!-- split: QA -->
<div class="abs photo" style="left:0;top:2847px;width:600px;height:405px;background:linear-gradient(135deg,#3c3a3a,#8c7a66 50%,#2f3a48)" role="img" aria-label="Photo: two professionals in a meeting reviewing a laptop"></div>
<section class="abs qa" style="left:671px;top:2938px;width:355px">
  <h2>QA Technology:</h2>
  <p>Prospora is a proprietary lead verification platform from Ledgerwise Reach that aims to sift out invalid leads with questionable or erroneous data. The platform is designed to equip sales teams with accurate, high-quality records in order to improve lead generation, accelerate pipeline and increase revenue.</p>
  <div class="btn-row">
    <a class="btn btn-solid" href="#">Learn More <span class="dot"></span></a>
    <a class="btn btn-ghost" href="#">Support <span class="dot"></span></a>
  </div>
</section>

<!-- stats -->
<section class="abs stats">
  <div class="abs stats-art" role="img" aria-label="Decorative abstract background in navy and warm orange tones"></div>
  <div class="abs stat" style="left:235px;top:92px"><h3>Downloads<br>Per Month</h3><p>Ticker to 70,000+</p></div>
  <div class="abs stat" style="left:235px;top:238px"><h3>Leads Delivered<br>Per Month</h3><p>Ticker 25,000+</p></div>
  <div class="abs stat" style="left:555px;top:155px"><h3>Countries We<br>Can Reach</h3><p>Ticker to 50+</p></div>
</section>

<!-- testimonials -->
<h2 class="abs sec-title" style="top:3862px;font-size:18px;font-weight:500">We've heard things like</h2>
<article class="abs quote-card">
  <div class="avatar" role="img" aria-label="Portrait placeholder for reviewer"></div>
  <h4>Tobin Farrow</h4>
  <div class="role">Project Manager</div>
  <p>What a load of rubbish bits and bobs pear shaped owt to do with me bubble and squeak jolly good morish tinkety tonk old fruit, car boot my good sir buggered plastered cheeky David, haggle young delinquent say so I said bite your arm off easy peasy. Skive off it's all gone to pot buggered.</p>
  <div class="dots"><span></span><span></span><span></span><span class="on"></span></div>
</article>
<div class="abs arrow" style="left:234px;top:4040px;background:var(--white);box-shadow:0 4px 14px rgba(30,40,80,.12)"><svg width="12" height="10" viewBox="0 0 12 10"><path d="M11 5H1M5 1L1 5l4 4" stroke="#6b7383" fill="none" stroke-width="1.3"/></svg></div>
<div class="abs arrow" style="left:934px;top:4040px;background:var(--sky)"><svg width="12" height="10" viewBox="0 0 12 10"><path d="M1 5h10M7 1l4 4-4 4" stroke="#fff" fill="none" stroke-width="1.3"/></svg></div>

<!-- footer -->
<footer class="abs footer"></footer>
<a class="abs f-logo" href="#">
  <span class="logo-mark" style="width:20px;height:20px"></span>
  <span class="logo-name">Ledgerwise Reach</span>
  <span class="logo-tag">The Demand Generation Company</span>
</a>
<p class="abs copy">Copyright © 2020 Ledgerwise Reach</p>
<div class="abs f-col" style="left:482px;top:4360px"><h5>Quick Link</h5><a href="#">Home</a><a href="#">About</a><a href="#">Services</a><a href="#">Support</a></div>
<div class="abs f-col" style="left:670px;top:4360px"><h5>Quick Link</h5><a href="#">Technology</a><a href="#">Intent Data</a><a href="#">Testimonials</a><a href="#">Contact Us</a></div>
<div class="abs f-col" style="left:859px;top:4360px"><h5>Follow Us</h5></div>
<div class="abs f-social"><span></span><span class="on"></span><span></span><span></span></div>

</body>
</html>
```